New Snazzy yet professinoal business card updated for todays consumer for a Real Estate Professional

I work in a family owned real estate business where we specialize in sales (buyer/seller) and property management. I would like a snazzy business card that will set me apart from other agents while maintaining its professional appearance. I would like to use the front and back of the card incorporating the business logo on the front with pictures and my personal logo on the back side. I have to have the TBNX symbol which I have attached. Card must be easy to read, distinguishable, and professional. Old card with contact information attached. My email has changed to Milo@MiloHathawayHomes.com

Target Market(s)

Home Sellers, Home Buyers, Business Professionals, Marketing Services,

Industry/Entity Type

Real Estate Agent

Contact Information for Business Card

Professional business card to stand apart from other agents while maintaining a professional appeal.

Font styles to use
Serif

Colors
ec1f27
fbee3e
0455a3

Requirements
Must have
• Must have contact information clear, easy to read. legible
Nice to have
• My picture.

```html
<!DOCTYPE html>
<html lang="en">
<head>
<meta charset="utf-8">
<title>Milo Hathaway Homes – Business Card</title>
<link href="https://fonts.googleapis.com/css2?family=Arimo:wght@400;700&family=Open+Sans:wght@400;600;700&display=swap" rel="stylesheet">
<style>
  :root {
    --page: #ece9e4;
    --card-light: #ffffff;
    --card-shade: #dcdde0;
    --blue: #2f64b0;
    --navy: #34488a;
    --text-blue: #2b4a92;
    --red: #b8283a;
    --yellow: #fbee3e;
    --rule: #8b8b8b;
    --photo: #7a7f84;
  }
  * { margin: 0; padding: 0; box-sizing: border-box; }
  html, body { width: 1200px; height: 1000px; overflow: hidden; }
  body { background: var(--page); position: relative; font-family: "Open Sans", Arial, sans-serif; }

  .card {
    position: absolute;
    width: 727px;
    height: 413px;
    overflow: hidden;
    background: radial-gradient(ellipse at 50% 35%, var(--card-light) 0%, #f1f1f3 45%, var(--card-shade) 100%);
    box-shadow: 0 2px 6px rgba(0,0,0,0.25);
  }
  .card-front { left: 235px; top: 32px; }
  .card-back  { left: 234px; top: 553px; }
  .card-swoosh { position: absolute; left: 0; top: 0; }

  /* front */
  .brand-mark {
    position: absolute; left: 112px; top: 198px;
    width: 46px; height: 46px; border-radius: 50%;
    background: var(--red);
  }
  .brand-name {
    position: absolute; left: 176px; top: 201px;
    font-family: "Arimo", Arial, sans-serif; font-weight: 400;
    color: var(--text-blue); font-size: 38px; line-height: 1;
    white-space: nowrap;
  }
  .brand-rule {
    position: absolute; left: 176px; top: 256px; width: 420px; height: 2px; background: var(--rule);
  }

  /* back */
  .office-mark {
    position: absolute; left: 34px; top: 152px; width: 34px; height: 34px; background: var(--red);
  }
  .office-name {
    position: absolute; left: 82px; top: 148px;
    font-family: "Open Sans", Arial, sans-serif; font-weight: 400;
    color: var(--text-blue); font-size: 38px; line-height: 1.1; white-space: nowrap;
  }

  .agent-photo {
    position: absolute; left: 524px; top: 105px; width: 138px; height: 164px;
    border: 5px solid var(--yellow);
    background: linear-gradient(180deg, #8d9196 0%, var(--photo) 55%, #2a2c33 100%);
  }
  .agent-name {
    position: absolute; left: 500px; top: 274px; width: 190px; text-align: center;
    font-size: 19px; color: var(--red); line-height: 1;
  }
  .agent-title {
    position: absolute; left: 500px; top: 296px; width: 190px; text-align: center;
    font-size: 11px; color: var(--text-blue); letter-spacing: 0.3px;
  }

  .contact-list { list-style: none; }
  .contact-item {
    position: absolute; font-size: 17px; color: var(--text-blue); line-height: 1; white-space: nowrap;
  }
  .contact-item::before {
    content: ""; position: absolute; left: -14px; top: 0; width: 8px; height: 10px; background: var(--yellow);
  }
  .office-phone { left: 58px; top: 313px; }
  .cell-phone   { left: 278px; top: 313px; }
  .fax          { left: 58px; top: 349px; }
  .email        { left: 278px; top: 349px; }

  .address-band {
    position: absolute; left: 0; top: 372px; width: 100%; height: 27px; background: var(--yellow);
  }
  .address {
    position: absolute; left: 58px; top: 5px;
    font-size: 14.5px; font-weight: 700; color: var(--text-blue); white-space: nowrap;
  }
  .listing-badge {
    position: absolute; left: 546px; top: 5px; width: 38px; height: 17px;
    background: #e6eaf2; border: 1px solid #9aa5bf;
  }
</style>
</head>
<body>

<section class="card card-front">
  <svg class="card-swoosh" width="727" height="413" viewBox="0 0 727 413" aria-hidden="true">
    <path d="M0 0 H727 V124 Q380 -20 0 140 Z" fill="var(--navy)"/>
    <path d="M0 0 H727 V98 Q380 -40 0 112 Z" fill="var(--blue)"/>
  </svg>
  <div class="brand-mark" aria-hidden="true"></div>
  <div class="brand-name">MILO HATHAWAY HOMES</div>
  <div class="brand-rule"></div>
</section>

<section class="card card-back">
  <svg class="card-swoosh" width="727" height="413" viewBox="0 0 727 413" aria-hidden="true">
    <path d="M0 0 H727 V112 Q380 -20 0 140 Z" fill="var(--navy)"/>
    <path d="M0 0 H727 V86 Q380 -40 0 112 Z" fill="var(--blue)"/>
  </svg>
  <div class="office-mark" aria-hidden="true"></div>
  <div class="office-name">Harbor Lane Realty</div>

  <div class="agent-photo" role="img" aria-label="Portrait photo of the agent"></div>
  <div class="agent-name">MILO HATHAWAY</div>
  <div class="agent-title">REALTOR, MBA, MPH</div>

  <ul class="contact-list">
    <li class="contact-item office-phone">Office: 555 310 2040</li>
    <li class="contact-item cell-phone">Cell: 555 318 7261</li>
    <li class="contact-item fax">Fax: 555 310 2047</li>
    <li class="contact-item email">Email: Milo@MiloHathawayHomes.com</li>
  </ul>

  <div class="address-band">
    <p class="address">Address: 24 Birchfield Plaza&nbsp; Lakewood, Oregon 97402</p>
    <div class="listing-badge" role="img" aria-label="TBNX listing badge"></div>
  </div>
</section>

</body>
</html>
```